Creative design for PLW Businesscard!

We would like a creative business card for our company The Maple Workshop. We situated in Barcelona and setup software development teams for companies in Belgium, Holland.

Orange is related to Holland.
PLW means cool in Dutch

* An Overview / Background of the Business & Services
o Setup and manage developer teams in Barcelona for for companies
in Holland, Belgium.
* The Target Market / Audience you are trying to reach
o Companies in Holland searching for developers
* Design Specifics; any preferences or ideas for Style, Colour,
Imagery, etc
o Orange, professional, fancy
o The Maple Workshop (PLW) means cool , good, nice

Target Market(s)

Companies in Holland searching for developers

Industry/Entity Type

Business

Contact Information for Business Card

Company name: The Maple Workshop

Name: Joost ter Haarveld

Title: Managing director (not necessary)

Email: joost@themapleworkshop.es

web: www.themapleworkshop.es

Phone: (+34) 932 487 113

Mobile: (+34) 668 302 947

Font styles to use
Other font styles liked:
• Bookman Old Style or Rockwell

Requirements
Must have
• Setup and manage developer teams in Barcelona for for companies
• in Holland, Belgium.

```html
<!DOCTYPE html>
<html lang="en">
<head>
<meta charset="utf-8">
<title>The Maple Workshop – Business Card</title>
<link rel="stylesheet" href="https://fonts.googleapis.com/css2?family=Arimo:ital,wght@0,400;0,700;1,400&display=swap">
<style>
  :root {
    --backdrop: #e8e8ea;
    --card: #ffffff;
    --orange: #ee8a3c;
    --ink: #1e1e1e;
    --muted: #6a6a6a;
  }
  * { box-sizing: border-box; margin: 0; padding: 0; }
  html, body {
    width: 847px; height: 1200px; overflow: hidden;
    background: var(--backdrop);
    font-family: "Arimo", Arial, sans-serif;
  }
  .sheet {
    position: relative; width: 847px; height: 1200px;
    display: flex; justify-content: center; align-items: center; gap: 44px;
  }
  .card {
    position: relative; width: 360px; height: 630px;
    background: var(--card);
    box-shadow: 0 6px 22px rgba(0,0,0,0.10);
  }
  .card--front .frame {
    position: absolute; inset: 12px;
    border: 2px dashed var(--orange);
  }
  .brand {
    position: absolute; top: 262px; left: 0; right: 0; text-align: center;
    font-weight: 700; font-size: 44px; letter-spacing: 4px;
    color: var(--ink); line-height: 1;
  }
  .company {
    position: absolute; top: 352px; left: 0; right: 0; text-align: center;
    font-weight: 700; font-size: 24px; color: var(--ink);
  }
  .front-web {
    position: absolute; bottom: 44px; left: 0; right: 0; text-align: center;
    font-size: 13px; color: var(--muted); letter-spacing: 0.3px;
  }
  .card--back .mark {
    position: absolute; top: 88px; left: 0; right: 0; text-align: center;
    font-weight: 700; font-size: 24px; letter-spacing: 3px;
    color: var(--ink); line-height: 1;
  }
  .person {
    position: absolute; top: 178px; left: 0; right: 0; text-align: center;
  }
  .person__name { font-weight: 700; font-size: 22px; color: var(--ink); }
  .person__role { font-style: italic; font-size: 13px; color: var(--muted); margin-top: 6px; }
  .contact {
    position: absolute; top: 318px; left: 0; right: 0; text-align: center;
    list-style: none; font-size: 13px; line-height: 1.65; color: var(--ink);
  }
  .tagline {
    position: absolute; bottom: 42px; left: 40px; right: 40px; text-align: center;
    font-size: 11px; line-height: 1.5; color: var(--muted);
  }
</style>
</head>
<body>
<main class="sheet">
  <section class="card card--front">
    <div class="frame"></div>
    <p class="brand">PLW</p>
    <p class="company">The Maple Workshop</p>
    <p class="front-web">www.themapleworkshop.es</p>
  </section>

  <section class="card card--back">
    <p class="mark">PLW</p>
    <div class="person">
      <p class="person__name">Joost ter Haarveld</p>
      <p class="person__role">Managing director</p>
    </div>
    <ul class="contact">
      <li>joost@themapleworkshop.es</li>
      <li>www.themapleworkshop.es</li>
      <li>(+34) 932 487 113</li>
      <li>(+34) 668 302 947</li>
    </ul>
    <p class="tagline">Setup and manage developer teams in Barcelona for companies in Holland, Belgium.</p>
  </section>
</main>
</body>
</html>
```